Poster for pawn shop lobby

Looking for green and gold as my colors, like the picture shown of my old poster. This time I'm contemplating with doing pictures as well as just text. Here are ideas of things I buy and give loans on. We want to emphasize jewelry, laptops, game systems, tools. I'm open-minded.
Old & Broken Gold
Jewelry & Collectibles
Diamonds
Video Games & Systems
Up-to-date Computers & Laptops
Tablets
Cameras
Power Tools
Home & Garden Equipment
Sports Equipment
Watches
Antique Collectibles
Musical Instruments
And anything else of value
Shop

```html
<!DOCTYPE html>
<html lang="en">
<head>
<meta charset="utf-8">
<title>We'll Loan or Pay You Cash On</title>
<link rel="stylesheet" href="https://fonts.googleapis.com/css2?family=Arimo:wght@700&family=Passion+One:wght@700&display=swap">
<style>
  :root {
    --green-deep: #137a34;
    --green-mid: #23913b;
    --green-light: #5cb83c;
    --gold-light: #fde55a;
    --gold-mid: #f3c81a;
    --gold-dark: #c99a06;
    --gold-text: #ffd83a;
    --coin: #f6b81c;
    --coin-edge: #1b1b1b;
    --red: #d4202a;
    --headline-green: #2fb34a;
    --ink: #111111;
    --white: #ffffff;
  }
  * { margin: 0; padding: 0; box-sizing: border-box; }
  html, body { width: 849px; height: 1200px; overflow: hidden; background: var(--green-mid); }
  .poster {
    position: relative;
    width: 849px;
    height: 1200px;
    overflow: hidden;
    background: linear-gradient(180deg, var(--green-deep) 15%, var(--green-mid) 55%, var(--green-light) 100%);
    font-family: "Arimo", Arial, sans-serif;
  }
  .header-band { position: absolute; left: 0; top: 0; width: 849px; height: 260px; }
  .gold-bars-art {
    position: absolute; left: 0; top: 0; width: 300px; height: 200px;
    background: radial-gradient(ellipse at 30% 35%, rgba(255,250,190,0.6) 0%, rgba(255,240,140,0) 70%);
  }
  .money-art {
    position: absolute; left: 0; top: 730px; width: 849px; height: 470px;
    background: linear-gradient(180deg, rgba(160,220,150,0) 0%, rgba(175,225,160,0.45) 45%, rgba(200,235,180,0.75) 100%);
  }
  .dollar-art {
    position: absolute; left: 480px; top: 730px; width: 369px; height: 470px;
    background: radial-gradient(ellipse at 60% 55%, rgba(236,214,90,0.85) 0%, rgba(215,200,80,0.5) 40%, rgba(200,210,90,0) 72%);
  }
  .headline {
    position: absolute; left: 0; right: 0; top: 38px;
    text-align: center;
    font-family: "Passion One", "Arial Black", sans-serif;
    font-weight: 700;
    line-height: 90px;
    letter-spacing: -2px;
  }
  .headline-line {
    display: block; font-size: 66px; color: var(--headline-green);
    -webkit-text-stroke: 3px var(--ink); paint-order: stroke fill;
    text-shadow: 3px 4px 0 var(--ink);
  }
  .headline-accent { color: var(--red); font-size: 76px; }
  .offer-list { position: absolute; left: 40px; top: 327px; list-style: none; }
  .offer-item {
    display: flex; align-items: center;
    height: 51px;
    font-size: 39px;
    font-weight: 700;
    color: var(--white);
    white-space: nowrap;
    text-shadow: 1px 2px 2px rgba(0,0,0,0.25);
  }
  .offer-item--featured { color: var(--gold-text); }
  .coin { width: 38px; height: 38px; margin-right: 19px; flex: none; }
  .featured-photos {
    position: absolute; left: 40px; top: 1052px;
    display: flex; gap: 22px;
  }
  .photo-slot {
    width: 124px; height: 124px; border-radius: 50%;
    border: 4px solid var(--gold-mid);
    box-shadow: 0 3px 8px rgba(0,0,0,0.3);
  }
  .photo-slot--jewelry { background: radial-gradient(circle at 40% 35%, #fff3b0, #d9a520 60%, #8a6410); }
  .photo-slot--laptop { background: radial-gradient(circle at 40% 35%, #e6ecef, #8b969c 60%, #3e464a); }
  .photo-slot--console { background: radial-gradient(circle at 40% 35%, #9aa3b0, #3b4049 60%, #15181c); }
  .photo-slot--tools { background: radial-gradient(circle at 40% 35%, #ffd27a, #e0741b 60%, #6b3508); }
</style>
</head>
<body>
<main class="poster">
  <div class="money-art" role="img" aria-label="Scattered banknotes fading into the background"></div>
  <div class="dollar-art" role="img" aria-label="Large golden 3D dollar sign"></div>

  <svg class="header-band" viewBox="0 0 849 260" aria-hidden="true">
    <defs>
      <linearGradient id="goldFill" x1="0" y1="0" x2="0" y2="1">
        <stop offset="0" stop-color="#fde55a"/>
        <stop offset="0.6" stop-color="#f3c81a"/>
        <stop offset="1" stop-color="#c99a06"/>
      </linearGradient>
      <symbol id="coin" viewBox="0 0 40 40">
        <circle cx="20" cy="20" r="18" fill="#f6b81c" stroke="#1b1b1b" stroke-width="2.5"/>
        <text x="20" y="28" text-anchor="middle" font-family="Arimo, Arial, sans-serif" font-weight="700" font-size="23" fill="#fff">$</text>
      </symbol>
    </defs>
    <path d="M0 0 H849 V150 Q430 300 0 138 Z" fill="url(#goldFill)"/>
    <path d="M0 138 Q430 300 849 150" fill="none" stroke="#0d5e27" stroke-width="6"/>
  </svg>
  <div class="gold-bars-art" role="img" aria-label="Stacked gold bullion bars in the top-left corner"></div>

  <h1 class="headline">
    <span class="headline-line">WE'LL <span class="headline-accent">LOAN</span> OR</span>
    <span class="headline-line">PAY YOU <span class="headline-accent">CASH</span> ON</span>
  </h1>

  <ul class="offer-list">
    <li class="offer-item"><svg class="coin"><use href="#coin"/></svg>Old &amp; Broken Gold</li>
    <li class="offer-item offer-item--featured"><svg class="coin"><use href="#coin"/></svg>Jewelry &amp; Collectibles</li>
    <li class="offer-item"><svg class="coin"><use href="#coin"/></svg>Diamonds</li>
    <li class="offer-item offer-item--featured"><svg class="coin"><use href="#coin"/></svg>Video Games &amp; Systems</li>
    <li class="offer-item offer-item--featured"><svg class="coin"><use href="#coin"/></svg>Up-to-date Computers &amp; Laptops</li>
    <li class="offer-item"><svg class="coin"><use href="#coin"/></svg>Tablets</li>
    <li class="offer-item"><svg class="coin"><use href="#coin"/></svg>Cameras</li>
    <li class="offer-item offer-item--featured"><svg class="coin"><use href="#coin"/></svg>Power Tools</li>
    <li class="offer-item"><svg class="coin"><use href="#coin"/></svg>Home &amp; Garden Equipment</li>
    <li class="offer-item"><svg class="coin"><use href="#coin"/></svg>Sports Equipment</li>
    <li class="offer-item"><svg class="coin"><use href="#coin"/></svg>Watches</li>
    <li class="offer-item"><svg class="coin"><use href="#coin"/></svg>Antique Collectibles</li>
    <li class="offer-item"><svg class="coin"><use href="#coin"/></svg>Musical Instruments</li>
    <li class="offer-item"><svg class="coin"><use href="#coin"/></svg>And anything else of value</li>
  </ul>

  <div class="featured-photos">
    <div class="photo-slot photo-slot--jewelry" role="img" aria-label="Photo of gold rings and necklaces"></div>
    <div class="photo-slot photo-slot--laptop" role="img" aria-label="Photo of a modern laptop"></div>
    <div class="photo-slot photo-slot--console" role="img" aria-label="Photo of a game console with controller"></div>
    <div class="photo-slot photo-slot--tools" role="img" aria-label="Photo of a cordless power drill"></div>
  </div>
</main>
</body>
</html>
```